Small Verses Across the Winter Years

Need a BOOK COVER, SPINE, and BACK for above named book. This is the story of my late wife (a university professor) told through her own songs and poems. It is about the people she loved, especially her grand children, her extensive professional and life interests, her family, friends, and festivities, her illness, etc.
Updates

Target Market(s)

Family and friends

Font styles to use
Other font styles liked:
• Times New Roman

Requirements
Must have
• Regret I haven't given much thought to it...
Nice to have
• Regret I haven't given much thought to it..
Should not have

```html
<!DOCTYPE html>
<html lang="en">
<head>
<meta charset="utf-8">
<title>Small Verses Across the Winter Years — Cover Wrap</title>
<link href="https://fonts.googleapis.com/css2?family=Great+Vibes&family=Noto+Serif:wght@400;700&display=swap" rel="stylesheet">
<style>
  :root {
    --wrap-red: #8b1a1c;
    --band-red: #cf2530;
    --title-pink: #f4a09a;
    --paper: #ffffff;
    --ink-dark: #2a1414;
    --ink-body: #222222;
    --script-red: #8b1a1c;
    --rule-red: #8b1a1c;
    --text-light: #ffffff;
    --rose-light: #e9a3a6;
    --rose-deep: #c42a33;
  }
  * { margin: 0; padding: 0; box-sizing: border-box; }
  html, body {
    width: 1200px; height: 873px; overflow: hidden;
    background: var(--wrap-red);
  }
  .cover-wrap {
    position: relative; width: 1200px; height: 873px;
    background: var(--wrap-red);
    font-family: "Noto Serif", "Times New Roman", serif;
  }

  /* Back cover */
  .back-panel {
    position: absolute; left: 0; top: 55px; width: 580px; height: 661px;
    background: var(--paper);
  }
  .back-title {
    position: absolute; left: 100px; top: 78px;
    font-family: "Great Vibes", cursive; font-weight: 400;
    font-size: 36px; line-height: 1; color: var(--script-red);
    word-spacing: 8px; white-space: nowrap;
  }
  .back-subtitle {
    position: absolute; left: 200px; top: 121px;
    font-size: 18px; line-height: 24px; color: var(--script-red);
  }
  .back-blurb {
    position: absolute; left: 101px; top: 180px; width: 368px;
    font-size: 12.4px; line-height: 16.5px; color: var(--ink-body);
  }
  .back-flowers {
    position: absolute; left: 0; top: 522px; width: 550px; height: 125px;
    background: linear-gradient(90deg, var(--rose-light) 0%, var(--rose-deep) 45%, var(--rose-light) 100%);
    opacity: .55;
  }

  /* Spine */
  .spine {
    position: absolute; left: 580px; top: 0; width: 48px; height: 873px;
  }
  .spine-title {
    position: absolute; left: 0; top: 66px; width: 48px;
    writing-mode: vertical-rl; white-space: nowrap;
    display: flex; align-items: center; line-height: 48px;
    color: var(--text-light);
  }
  .spine-title .script { font-family: "Great Vibes", cursive; font-size: 30px; margin-bottom: 12px; word-spacing: 6px; }
  .spine-title .serif { font-size: 21px; }
  .spine-author {
    position: absolute; left: 0; top: 566px; width: 48px;
    writing-mode: vertical-rl; line-height: 48px; white-space: nowrap;
    font-size: 16px; letter-spacing: 1px; color: var(--text-light);
  }

  /* Front cover */
  .front-ornament {
    position: absolute; left: 710px; width: 415px; height: 20px;
  }
  .front-ornament.top { top: 24px; }
  .front-ornament.bottom { top: 825px; }
  .title-block {
    position: absolute; left: 628px; top: 55px; width: 572px; height: 295px;
    background: var(--title-pink);
  }
  .title-script {
    position: absolute; font-family: "Great Vibes", cursive; font-weight: 400;
    color: var(--text-light); font-size: 112px; line-height: 1; white-space: nowrap;
  }
  .title-script.line-one { left: 40px; top: 30px; }
  .title-script.line-two { left: 170px; top: 115px; }
  .title-subtitle {
    position: absolute; left: 0; top: 215px; width: 588px; text-align: center;
    font-size: 31px; letter-spacing: .5px; color: var(--ink-dark);
  }
  .title-rule {
    position: absolute; left: 67px; top: 262px; width: 453px; height: 4px;
    background: var(--rule-red);
  }
  .cover-photo {
    position: absolute; left: 628px; top: 350px; width: 572px; height: 368px;
    background: linear-gradient(180deg, #7d7aa0 0%, #b39ab0 12%, #e0a684 24%, #3c3440 30%, #2a2630 40%, #8a7a94 52%, #5a5068 68%, #1e1a1c 85%, #151213 100%);
  }
  .author-band {
    position: absolute; left: 628px; top: 718px; width: 572px; height: 97px;
    background: var(--band-red);
    display: flex; align-items: center; justify-content: center;
  }
  .author-name {
    color: var(--text-light); font-size: 24px; letter-spacing: 1.5px;
    text-shadow: 0 2px 3px rgba(0,0,0,.35);
  }
</style>
</head>
<body>
<div class="cover-wrap">

  <section class="back-panel">
    <h2 class="back-title">Small Verses</h2>
    <p class="back-subtitle">Across the Winter Years</p>
    <p class="back-blurb">It is the story of a university professor told through her own songs and poems. It is about the people she loved, especially her grand children, her extensive professional and life interests, her family, friends, and festivities, her illness, etc.</p>
    <div class="back-flowers" role="img" aria-label="Red rose with scattered petals"></div>
  </section>

  <section class="spine">
    <div class="spine-title"><span class="script">Small Verses</span><span class="serif">Across the Winter Years</span></div>
    <div class="spine-author">LALITA DESHMUKH RAO</div>
  </section>

  <svg class="front-ornament top" viewBox="0 0 415 20">
    <line x1="0" y1="10" x2="145" y2="10" stroke="#fff" stroke-width="2"/>
    <line x1="235" y1="10" x2="415" y2="10" stroke="#fff" stroke-width="2"/>
    <rect x="150" y="1" width="80" height="18" rx="4" fill="#a2383a" role="img" aria-label="Scroll ornament"/>
  </svg>

  <section class="title-block">
    <h1 class="title-script line-one">Small</h1>
    <span class="title-script line-two">Verses</span>
    <p class="title-subtitle">Across the Winter Years</p>
    <div class="title-rule"></div>
  </section>

  <div class="cover-photo" role="img" aria-label="Lakeside at dusk with a wooden rowboat moored by a small jetty"></div>

  <div class="author-band"><p class="author-name">LALITA DESHMUKH RAO</p></div>

  <svg class="front-ornament bottom" viewBox="0 0 415 20">
    <line x1="0" y1="10" x2="145" y2="10" stroke="#fff" stroke-width="2"/>
    <line x1="235" y1="10" x2="415" y2="10" stroke="#fff" stroke-width="2"/>
    <rect x="150" y="1" width="80" height="18" rx="4" fill="#a2383a" role="img" aria-label="Scroll ornament"/>
  </svg>

</div>
</body>
</html>
```